Corvath Brazilian/Portuguese Restaurant Outdoor Flag

We need a flag design that is 72" tall by 20" wide for our restaurant.
We want to draw the eye and be visually striking while not appearing overly Brazilian but also not disrespecting our Portuguese roots.
Not wordy and tilted towards luxury. We want to move closer to a luxury brand and therefore want flags that would fly outside of a Gold Lantern or Vandrel Court rather than a Tolvex or Quiet Brook

Target Market(s)

Luxury

Industry/Entity Type

Restaurant

Colors
0054AA
0677BA
7BADD7
CADEEF
E8F1F8
00AB8E
00BBA5
67D7C9
C6EFE9
E9F9F6
FFF300
FFF600
FEFA6F
FFFEC7
FFFEE8

```html
<!DOCTYPE html>
<html lang="en">
<head>
<meta charset="utf-8">
<title>Corvath Restaurant — Outdoor Feather Flags</title>
<link rel="stylesheet" href="https://fonts.googleapis.com/css2?family=Syncopate:wght@700&family=Playfair+Display:wght@900&display=swap">
<style>
  :root {
    --blue: #1457a8;
    --yellow: #f6ec25;
    --white: #ffffff;
    --pole: #000000;
  }
  html, body {
    margin: 0;
    padding: 0;
    width: 1109px;
    height: 1200px;
    overflow: hidden;
    background: var(--white);
  }
  .flag-set {
    display: block;
    width: 1109px;
    height: 1200px;
  }
  .pole { fill: var(--pole); }
  .pole-spike { stroke: var(--pole); stroke-width: 6; }
  .wordmark {
    font-family: "Syncopate", "Arial Black", sans-serif;
    font-weight: 700;
    font-size: 176px;
  }
  .restaurant-line {
    font-family: "Playfair Display", Georgia, serif;
    font-weight: 900;
    font-size: 62px;
  }
  .badge-name {
    font-family: "Syncopate", "Arial Black", sans-serif;
    font-weight: 700;
    font-size: 42px;
  }
  .ink-blue { fill: var(--blue); }
  .ink-yellow { fill: var(--yellow); }
  .ink-white { fill: var(--white); }
  .badge-disc { fill: var(--blue); }
</style>
</head>
<body>
<svg class="flag-set" viewBox="0 0 1836 1988" xmlns="http://www.w3.org/2000/svg">
  <defs>
    <linearGradient id="fill-citrus" x1="0" y1="0" x2="0" y2="1">
      <stop offset="0" stop-color="#14ae95"/>
      <stop offset="0.35" stop-color="#8cc56f"/>
      <stop offset="0.7" stop-color="#c9da55"/>
      <stop offset="1" stop-color="#f6ec25"/>
    </linearGradient>
    <linearGradient id="fill-lagoon" x1="0" y1="0" x2="0" y2="1">
      <stop offset="0" stop-color="#15ad93"/>
      <stop offset="0.58" stop-color="#15ad93"/>
      <stop offset="0.68" stop-color="#0b8a9f"/>
      <stop offset="0.8" stop-color="#1457a8"/>
      <stop offset="1" stop-color="#1457a8"/>
    </linearGradient>
    <linearGradient id="foliage-citrus" x1="1" y1="0" x2="0" y2="1">
      <stop offset="0" stop-color="#1f9f9a"/>
      <stop offset="0.5" stop-color="#5fae86"/>
      <stop offset="1" stop-color="#a3c866"/>
    </linearGradient>
    <linearGradient id="foliage-ocean" x1="1" y1="0" x2="0" y2="1">
      <stop offset="0" stop-color="#7ba3d6"/>
      <stop offset="0.5" stop-color="#3f78c2"/>
      <stop offset="1" stop-color="#1a5cad"/>
    </linearGradient>
    <linearGradient id="foliage-lagoon" x1="1" y1="0" x2="0" y2="1">
      <stop offset="0" stop-color="#1f8fa6"/>
      <stop offset="0.5" stop-color="#14a294"/>
      <stop offset="1" stop-color="#1a7fa3"/>
    </linearGradient>
  </defs>

  <!-- Flag: citrus edition -->
  <g class="flag flag-citrus">
    <line class="pole-spike" x1="127" y1="1530" x2="127" y2="1832"/>
    <path class="pole" d="M118,1532 V530 A392,385 0 0 1 510,145 V1532 Z"/>
    <path d="M135,1532 V530 A375,368 0 0 1 510,162 V1532 Z" fill="url(#fill-citrus)"/>
    <path role="img" aria-label="Line-drawn tropical foliage in deep blue strokes with a white macaw perched across the seal" d="M135,945 V530 A375,368 0 0 1 510,162 V945 Z" fill="url(#foliage-citrus)"/>
    <g class="badge">
      <circle class="badge-disc" cx="323" cy="522" r="163"/>
      <text class="badge-name ink-white" x="323" y="537" text-anchor="middle" textLength="250" lengthAdjust="spacingAndGlyphs">CORVATH</text>
    </g>
    <g class="ink-blue">
      <text class="wordmark" x="158" y="1102" textLength="344" lengthAdjust="spacingAndGlyphs">COR</text>
      <text class="wordmark" x="158" y="1250" textLength="271" lengthAdjust="spacingAndGlyphs">VA</text>
      <text class="wordmark" x="158" y="1399" textLength="309" lengthAdjust="spacingAndGlyphs">TH</text>
      <text class="restaurant-line" x="153" y="1481" textLength="340" lengthAdjust="spacingAndGlyphs">RESTAURANT</text>
    </g>
  </g>

  <!-- Flag: ocean edition -->
  <g class="flag flag-ocean" transform="translate(600 0)">
    <line class="pole-spike" x1="127" y1="1530" x2="127" y2="1832"/>
    <path class="pole" d="M118,1532 V530 A392,385 0 0 1 510,145 V1532 Z"/>
    <path d="M135,1532 V530 A375,368 0 0 1 510,162 V1532 Z" fill="var(--blue)"/>
    <path role="img" aria-label="White line-drawn tropical foliage on blue with a yellow macaw perched across the seal" d="M135,945 V530 A375,368 0 0 1 510,162 V945 Z" fill="url(#foliage-ocean)"/>
    <g class="badge">
      <circle class="badge-disc" cx="323" cy="522" r="163"/>
      <text class="badge-name ink-yellow" x="323" y="537" text-anchor="middle" textLength="250" lengthAdjust="spacingAndGlyphs">CORVATH</text>
    </g>
    <g class="ink-yellow">
      <text class="wordmark" x="158" y="1102" textLength="344" lengthAdjust="spacingAndGlyphs">COR</text>
      <text class="wordmark" x="158" y="1250" textLength="271" lengthAdjust="spacingAndGlyphs">VA</text>
      <text class="wordmark" x="158" y="1399" textLength="309" lengthAdjust="spacingAndGlyphs">TH</text>
      <text class="restaurant-line" x="153" y="1481" textLength="340" lengthAdjust="spacingAndGlyphs">RESTAURANT</text>
    </g>
  </g>

  <!-- Flag: lagoon edition -->
  <g class="flag flag-lagoon" transform="translate(1200 0)">
    <line class="pole-spike" x1="127" y1="1530" x2="127" y2="1832"/>
    <path class="pole" d="M118,1532 V530 A392,385 0 0 1 510,145 V1532 Z"/>
    <path d="M135,1532 V530 A375,368 0 0 1 510,162 V1532 Z" fill="url(#fill-lagoon)"/>
    <path role="img" aria-label="Blue line-drawn tropical foliage on teal with a white macaw perched across the seal" d="M135,945 V530 A375,368 0 0 1 510,162 V945 Z" fill="url(#foliage-lagoon)"/>
    <g class="badge">
      <circle class="badge-disc" cx="323" cy="522" r="163"/>
      <text class="badge-name ink-white" x="323" y="537" text-anchor="middle" textLength="250" lengthAdjust="spacingAndGlyphs">CORVATH</text>
    </g>
    <g class="ink-white">
      <text class="wordmark" x="158" y="1102" textLength="344" lengthAdjust="spacingAndGlyphs">COR</text>
      <text class="wordmark" x="158" y="1250" textLength="271" lengthAdjust="spacingAndGlyphs">VA</text>
      <text class="wordmark" x="158" y="1399" textLength="309" lengthAdjust="spacingAndGlyphs">TH</text>
      <text class="restaurant-line" x="153" y="1481" textLength="340" lengthAdjust="spacingAndGlyphs">RESTAURANT</text>
    </g>
  </g>
</svg>
</body>
</html>
```